Business Card Design

Company is a Commercial Building Company specialising in New Construction and existing refurbishments

Industry/Entity Type

Business

Contact Information for Business Card

Dale Mercer
Construction Manager
E Dale@harbridgebuilding.com.au
M 0400 213 947
Mail 27 Tarrant Rise Kestrel Point WA 6218

```html
<!DOCTYPE html>
<html lang="en">
<head>
<meta charset="utf-8">
<title>Harbridge Building &amp; Construction — Business Card</title>
<link rel="stylesheet" href="https://fonts.googleapis.com/css2?family=Mulish:wght@400;700;800&display=swap">
<style>
  :root {
    --backdrop: #e6e6e4;
    --card-white: #ffffff;
    --brand-cyan: #1db6d6;
    --brand-orange: #f0892a;
    --ink-navy: #2b2f3f;
    --ink-grey: #5c606b;
    --card-shadow: 0 14px 30px rgba(0, 0, 0, 0.14);
  }
  * { box-sizing: border-box; margin: 0; padding: 0; }
  html, body {
    width: 1200px;
    height: 856px;
    overflow: hidden;
    background: var(--backdrop);
    font-family: "Mulish", Arial, sans-serif;
  }
  .canvas {
    position: relative;
    width: 1200px;
    height: 856px;
    display: flex;
    align-items: center;
    justify-content: center;
    gap: 60px;
  }
  .card {
    width: 520px;
    height: 298px;
    border-radius: 26px;
    box-shadow: var(--card-shadow);
    position: relative;
    overflow: hidden;
  }
  .card--front {
    background: var(--card-white);
    display: flex;
    align-items: center;
    justify-content: space-between;
    padding: 0 28px 0 32px;
  }
  .card--back {
    background: var(--brand-cyan);
    display: flex;
    align-items: center;
    justify-content: center;
  }

  .brand {
    display: flex;
    align-items: center;
    gap: 10px;
    flex: none;
  }
  .brand__square {
    width: 28px;
    height: 28px;
    background: var(--brand-cyan);
    flex: none;
  }
  .brand__name {
    font-weight: 700;
    font-size: 15px;
    line-height: 1.2;
    color: var(--ink-navy);
    text-transform: uppercase;
    letter-spacing: 0.2px;
    white-space: nowrap;
  }
  .card--back .brand__name {
    color: var(--card-white);
    font-size: 20px;
    text-align: center;
  }

  .contact {
    flex: none;
  }
  .contact__name {
    font-weight: 800;
    font-size: 14px;
    color: var(--brand-cyan);
    text-transform: uppercase;
    letter-spacing: 0.3px;
  }
  .contact__role {
    font-weight: 400;
    font-size: 13px;
    color: var(--ink-grey);
    margin: 3px 0 10px;
  }
  .contact__list { list-style: none; }
  .contact__item {
    display: flex;
    align-items: flex-start;
    gap: 7px;
    font-weight: 700;
    font-size: 12px;
    line-height: 1.45;
    color: var(--ink-navy);
    white-space: nowrap;
  }
  .contact__icon {
    flex: none;
    width: 12px;
    height: 12px;
    margin-top: 3px;
  }
</style>
</head>
<body>
  <main class="canvas">
    <section class="card card--front" aria-label="Business card front">
      <div class="brand">
        <span class="brand__square" aria-hidden="true"></span>
        <span class="brand__name">Harbridge Building<br>&amp; Construction</span>
      </div>
      <div class="contact">
        <p class="contact__name">Dale Mercer</p>
        <p class="contact__role">Construction Manager</p>
        <ul class="contact__list">
          <li class="contact__item">
            <svg class="contact__icon" viewBox="0 0 12 12" aria-hidden="true">
              <circle cx="6" cy="6" r="6" fill="var(--brand-orange)"/>
              <rect x="3" y="4" width="6" height="4.2" fill="none" stroke="#fff" stroke-width="0.9"/>
              <path d="M3 4 L6 6.4 L9 4" fill="none" stroke="#fff" stroke-width="0.9"/>
            </svg>
            <span>dale@harbridgebuilding.com.au</span>
          </li>
          <li class="contact__item">
            <svg class="contact__icon" viewBox="0 0 12 12" aria-hidden="true">
              <circle cx="6" cy="6" r="6" fill="var(--brand-orange)"/>
              <path d="M4 3.2 L5.2 3.2 L5.6 4.8 L4.9 5.3 Q5.6 6.7 6.8 7.2 L7.3 6.5 L8.8 6.9 L8.8 8.1 Q5.5 8.6 3.9 4.6 Z" fill="#fff"/>
            </svg>
            <span>0400 213 947</span>
          </li>
          <li class="contact__item">
            <svg class="contact__icon" viewBox="0 0 12 12" aria-hidden="true">
              <circle cx="6" cy="6" r="6" fill="var(--brand-orange)"/>
              <path d="M6 2.6 A2.2 2.2 0 0 1 8.2 4.8 Q8.2 6.4 6 9.3 Q3.8 6.4 3.8 4.8 A2.2 2.2 0 0 1 6 2.6 Z" fill="#fff"/>
              <circle cx="6" cy="4.8" r="0.8" fill="var(--brand-orange)"/>
            </svg>
            <span>27 Tarrant Rise<br>Kestrel Point WA 6218</span>
          </li>
        </ul>
      </div>
    </section>

    <section class="card card--back" aria-label="Business card back">
      <span class="brand__name">Harbridge Building<br>&amp; Construction</span>
    </section>
  </main>
</body>
</html>
```